Postcard Design

We are an online real estate agent referral service. The client goes online and fills out basic information on themselves and their projected housing needs. We then locate an agent in their desired area that matches their profile. Contact information is then sent to the Realtor and the client so they can coordinate their move. The service is free to the client; our fee is paid by the agent upon a successful closing. The web site is www.kvlp.us.

Industry/Entity Type

Real Estate

```html
<!DOCTYPE html>
<html lang="en">
<head>
<meta charset="utf-8">
<title>Key Valley Location Partners — Postcard</title>
<link href="https://fonts.googleapis.com/css2?family=Oswald:wght@500;700&family=Open+Sans:wght@400;600;700&display=swap" rel="stylesheet">
<style>
  :root{
    --orange:#f26a1b;
    --orange-dark:#d9560c;
    --charcoal:#3a3a3c;
    --charcoal-deep:#2b2b2d;
    --paper:#ffffff;
    --ink:#4a4a4a;
    --stage:#ececec;
  }
  *{box-sizing:border-box;margin:0;padding:0}
  html,body{width:900px;height:1200px;overflow:hidden;background:var(--stage)}
  body{position:relative;font-family:"Open Sans",Arial,sans-serif;color:var(--ink)}
  .card{position:absolute;left:40px;width:820px;background:var(--paper);overflow:hidden;box-shadow:0 6px 18px rgba(0,0,0,.18)}
  .front{top:40px;height:520px}
  .back{top:600px;height:560px}

  /* front */
  .brand{position:absolute;left:36px;top:34px;display:flex;align-items:center;gap:12px}
  .brand-mark{width:22px;height:22px;background:var(--orange)}
  .brand-name{font-family:"Open Sans",Arial,sans-serif;font-weight:700;font-size:17px;line-height:1.25;color:var(--charcoal);width:190px}
  .hero-photo{position:absolute;left:400px;top:0;width:420px;height:430px;
    background:linear-gradient(180deg,#9cc3e6 0%,#cfe1ef 38%,#b59a7f 55%,#8f7660 72%,#5f8a3e 88%,#4e7a32 100%);
    clip-path:polygon(24% 0,100% 0,100% 100%,0 100%)}
  .front-accents{position:absolute;left:0;top:0}
  .headline-band{position:absolute;left:0;top:170px;width:470px;height:124px;background:var(--orange);
    clip-path:polygon(0 0,100% 0,88% 100%,0 100%)}
  .headline{position:absolute;left:36px;top:180px;font-family:"Oswald",Arial,sans-serif;font-weight:700;font-size:50px;line-height:1.04;color:#fff;letter-spacing:.5px;text-transform:uppercase}
  .benefits{position:absolute;left:36px;top:310px;list-style:none}
  .benefits li{display:flex;gap:12px;align-items:flex-start;margin-bottom:12px;font-weight:700;font-size:18px;line-height:1.2;color:var(--orange-dark);width:250px}
  .benefits svg{flex:none;margin-top:2px}
  .box-photo{position:absolute;left:290px;top:312px;width:115px;height:88px;background:linear-gradient(160deg,#d6b384,#b48a57)}
  .footer-band{position:absolute;left:0;top:430px;width:820px;height:46px;background:var(--orange)}
  .footer-dark{position:absolute;left:0;top:476px;width:820px;height:44px;background:var(--charcoal)}
  .web{position:absolute;right:40px;top:440px;display:flex;align-items:center;gap:10px;color:#fff;font-weight:700;font-size:20px}

  /* back */
  .back-left{position:absolute;left:0;top:0;width:410px;height:560px}
  .back-divider{position:absolute;left:410px;top:30px;width:1px;height:500px;background:#e3e3e3}
  .about-photo{position:absolute;left:30px;top:24px;width:360px;height:150px;
    background:linear-gradient(180deg,#a9c9e6 0%,#d8e6f0 35%,#8b5a45 55%,#6e4636 75%,#5b8a3c 100%)}
  .about-accent{position:absolute;left:0;top:140px}
  .about-title{position:absolute;left:30px;top:200px;font-family:"Oswald",Arial,sans-serif;font-weight:700;font-size:26px;color:var(--charcoal);letter-spacing:.5px}
  .about-text{position:absolute;left:30px;top:244px;width:355px;font-size:12.5px;line-height:1.5}
  .about-list{position:absolute;left:30px;top:330px;width:355px;list-style:none;font-size:12.5px;line-height:1.5}
  .about-list li{display:flex;gap:8px;margin-bottom:8px}
  .about-list svg{flex:none;margin-top:3px}
  .contact-band{position:absolute;left:0;top:440px;width:410px;height:96px;background:var(--charcoal);
    display:grid;grid-template-columns:1.3fr 1fr;gap:10px 14px;padding:16px 24px;color:#fff;font-size:11.5px;line-height:1.4}
  .contact-band div{display:flex;gap:8px;align-items:flex-start}
  .contact-band svg{flex:none}
  .back-strip{position:absolute;left:0;top:536px;width:410px;height:24px;background:var(--orange)}
</style>
</head>
<body>

<section class="card front">
  <div class="hero-photo" role="img" aria-label="Photo of a two-story suburban house with a green lawn under a blue sky"></div>
  <svg class="front-accents" width="820" height="430" viewBox="0 0 820 430">
    <polygon points="470,0 500,0 400,430 370,430" fill="var(--charcoal)"/>
    <polygon points="440,0 462,0 362,430 340,430" fill="var(--orange)"/>
    <polygon points="0,0 26,0 0,26" fill="var(--charcoal)"/>
  </svg>

  <div class="brand">
    <span class="brand-mark"></span>
    <span class="brand-name">Key Valley Location Partners</span>
  </div>

  <div class="headline-band"></div>
  <h1 class="headline">Relocation<br>Specialist</h1>

  <ul class="benefits">
    <li>
      <svg width="20" height="20" viewBox="0 0 20 20"><path d="M3 10l5 5 9-11" fill="none" stroke="var(--orange)" stroke-width="3.5" stroke-linecap="round" stroke-linejoin="round"/></svg>
      <span>Take advantage of our FREE SERVICE</span>
    </li>
    <li>
      <svg width="20" height="20" viewBox="0 0 20 20"><path d="M3 10l5 5 9-11" fill="none" stroke="var(--orange)" stroke-width="3.5" stroke-linecap="round" stroke-linejoin="round"/></svg>
      <span>We match you with the right agent</span>
    </li>
  </ul>
  <div class="box-photo" role="img" aria-label="Cardboard moving box labelled relocation"></div>

  <div class="footer-band"></div>
  <div class="footer-dark"></div>
  <div class="web">
    <svg width="24" height="24" viewBox="0 0 24 24" fill="none" stroke="#fff" stroke-width="2"><circle cx="12" cy="12" r="10"/><ellipse cx="12" cy="12" rx="4.5" ry="10"/><path d="M2 12h20M4 7h16M4 17h16"/></svg>
    <span>www.kvlp.us</span>
  </div>
</section>

<section class="card back">
  <div class="back-left">
    <div class="about-photo" role="img" aria-label="Photo of a brick family home with a front lawn"></div>
    <svg class="about-accent" width="410" height="50" viewBox="0 0 410 50">
      <polygon points="0,14 130,34 130,44 0,24" fill="var(--charcoal)"/>
      <polygon points="0,26 170,50 0,50" fill="var(--orange)"/>
    </svg>
    <h2 class="about-title">ABOUT US</h2>
    <p class="about-text">Key Valley Location Partners is designed to help make the real estate phase of your move as easy as possible. We find a qualified broker specializing in your chosen area by using the information you provide us.</p>
    <ul class="about-list">
      <li><svg width="10" height="10" viewBox="0 0 10 10"><path d="M1 5l3 3 5-7" fill="none" stroke="var(--orange)" stroke-width="2"/></svg><span>You will be able to communicate with the broker and coordinate your move in advance.</span></li>
      <li><svg width="10" height="10" viewBox="0 0 10 10"><path d="M1 5l3 3 5-7" fill="none" stroke="var(--orange)" stroke-width="2"/></svg><span>We can either provide you the broker's contact information or have them contact you.</span></li>
    </ul>
    <div class="contact-band">
      <div>
        <svg width="14" height="16" viewBox="0 0 14 16"><path d="M7 1a5 5 0 0 1 5 5c0 4-5 9-5 9S2 10 2 6a5 5 0 0 1 5-5z" fill="var(--orange)"/><circle cx="7" cy="6" r="1.8" fill="var(--charcoal)"/></svg>
        <span>428 W. Aspen Grove Lane<br>Littleton CO 80120</span>
      </div>
      <div>
        <svg width="14" height="14" viewBox="0 0 14 14"><path d="M3 1l2.5 3-1.5 1.5a8 8 0 0 0 4.5 4.5L10 8.5l3 2.5-1.5 2C6 13 1 8 1 2.5z" fill="var(--orange)"/></svg>
        <span>720-555-0148</span>
      </div>
      <div>
        <svg width="14" height="12" viewBox="0 0 14 12"><rect x="1" y="1" width="12" height="10" fill="var(--orange)"/><path d="M1 1l6 5 6-5" fill="none" stroke="var(--charcoal)" stroke-width="1.3"/></svg>
        <span>info@kvlp.us</span>
      </div>
      <div>
        <svg width="14" height="14" viewBox="0 0 24 24" fill="none" stroke="var(--orange)" stroke-width="2.5"><circle cx="12" cy="12" r="10"/><ellipse cx="12" cy="12" rx="4.5" ry="10"/><path d="M2 12h20"/></svg>
        <span>www.kvlp.us</span>
      </div>
    </div>
    <div class="back-strip"></div>
  </div>
  <div class="back-divider"></div>
</section>

</body>
</html>
```